Harborline Motors LLC

Car Dealer Customer Service
Address: 2741 Linden Avenue, Shelbyville, TN 37162
web: www.harborlinemotorstn.net
email: harborlinemotorstn@mailbox-example.net
Phone: (931) 555-0148
Phone: (629) 555-0173

```html
<!DOCTYPE html>
<html lang="en">
<head>
<meta charset="utf-8">
<title>Harborline Motors LLC – Business Card</title>
<link rel="stylesheet" href="https://fonts.googleapis.com/css2?family=Montserrat:wght@300;400;800&display=swap">
<style>
  :root {
    --sky-blue: #2a92cb;
    --deep-blue: #1d78a9;
    --ink-blue: #1a6fa3;
    --gold: #ebb144;
    --gold-light: #f1c268;
    --paper: #ffffff;
    --canvas: #f6f6f6;
  }
  * { margin: 0; padding: 0; box-sizing: border-box; }
  html, body {
    width: 800px; height: 1200px; overflow: hidden;
    background: var(--canvas);
    font-family: "Montserrat", sans-serif;
  }
  .sheet { position: relative; width: 800px; height: 1200px; }
  .card {
    position: absolute; left: 50px; width: 700px; height: 400px;
    background: var(--paper); overflow: hidden;
    box-shadow: 0 3px 10px rgba(0,0,0,0.18);
  }
  .card--front { top: 160px; }
  .card--back { top: 640px; }
  .card__shapes { position: absolute; inset: 0; }

  .front__name {
    position: absolute; left: 41px; top: 78px;
    font-weight: 800; font-size: 31px; letter-spacing: 0.3px;
    color: var(--ink-blue); text-transform: uppercase; white-space: nowrap;
  }
  .contact-list {
    position: absolute; left: 41px; top: 160px;
    list-style: none; color: var(--ink-blue);
    font-weight: 300; font-size: 15.5px; line-height: 1.3;
  }
  .contact-list li { display: flex; align-items: flex-start; margin-bottom: 10px; }
  .contact-list svg { width: 13px; height: 13px; margin: 3px 12px 0 0; flex: none; fill: var(--ink-blue); }

  .brand-mark {
    position: absolute; display: flex; flex-direction: column; align-items: center;
    color: var(--ink-blue); font-weight: 800; text-transform: uppercase; white-space: nowrap;
  }
  .brand-mark__dot { border-radius: 50%; background: var(--deep-blue); }
  .brand-mark--front { left: 420px; top: 88px; width: 200px; font-size: 17px; }
  .brand-mark--front .brand-mark__dot { width: 130px; height: 130px; margin-bottom: 14px; }
  .brand-mark--back { left: 438px; top: 168px; width: 200px; font-size: 20px; }
  .brand-mark--back .brand-mark__dot { width: 90px; height: 90px; margin-bottom: 14px; }
</style>
</head>
<body>
<main class="sheet">

  <section class="card card--front" aria-label="Card front">
    <svg class="card__shapes" viewBox="0 0 700 400" aria-hidden="true">
      <rect x="0" y="0" width="700" height="52" fill="var(--sky-blue)"/>
      <polygon points="0,347 629,347 700,262 700,400 0,400" fill="var(--deep-blue)"/>
    </svg>
    <h1 class="front__name">Harborline Motors</h1>
    <ul class="contact-list">
      <li>
        <svg viewBox="0 0 24 24"><path d="M6.6 10.8a15 15 0 0 0 6.6 6.6l2.2-2.2a1 1 0 0 1 1-.25 11.4 11.4 0 0 0 3.6.6 1 1 0 0 1 1 1V20a1 1 0 0 1-1 1A17 17 0 0 1 3 4a1 1 0 0 1 1-1h3.5a1 1 0 0 1 1 1c0 1.25.2 2.450.6 3.6a1 1 0 0 1-.25 1z"/></svg>
        <span>(931) 555-0148 / (629) 555-0173</span>
      </li>
      <li>
        <svg viewBox="0 0 24 24"><path d="M2 5h20v14H2z" fill="var(--ink-blue)"/><path d="M3 6l9 7 9-7" fill="none" stroke="#fff" stroke-width="1.6"/></svg>
        <span>harborlinemotorstn@mailbox-example.net</span>
      </li>
      <li>
        <svg viewBox="0 0 24 24"><path d="M12 2a7 7 0 0 0-7 7c0 5 7 13 7 13s7-8 7-13a7 7 0 0 0-7-7zm0 9.5A2.5 2.5 0 1 1 12 6.5a2.5 2.5 0 0 1 0 5z"/></svg>
        <span>2741 Linden Avenue, Shelbyville<br>TN 37162</span>
      </li>
      <li>
        <svg viewBox="0 0 24 24"><circle cx="12" cy="12" r="9.5" fill="none" stroke="var(--ink-blue)" stroke-width="2"/><path d="M2.5 12h19M12 2.5c-3 3-3 16 0 19M12 2.5c3 3 3 16 0 19" fill="none" stroke="var(--ink-blue)" stroke-width="1.6"/></svg>
        <span>www.harborlinemotorstn.net</span>
      </li>
    </ul>
    <div class="brand-mark brand-mark--front">
      <span class="brand-mark__dot"></span>
      <span>Harborline Motors</span>
    </div>
  </section>

  <section class="card card--back" aria-label="Card back">
    <svg class="card__shapes" viewBox="0 0 700 400">
      <defs>
        <linearGradient id="feature-fill" x1="0" y1="0" x2="1" y2="1">
          <stop offset="0" stop-color="var(--gold-light)"/>
          <stop offset="1" stop-color="var(--gold)"/>
        </linearGradient>
      </defs>
      <polygon points="0,0 700,0 700,100 477,100 331,280 0,280" fill="var(--sky-blue)" aria-hidden="true"/>
      <rect x="0" y="358" width="700" height="42" fill="var(--sky-blue)" aria-hidden="true"/>
      <rect x="0" y="30" width="360" height="222" fill="url(#feature-fill)" role="img" aria-label="Large brand illustration area"/>
    </svg>
    <div class="brand-mark brand-mark--back">
      <span class="brand-mark__dot"></span>
      <span>Harborline Motors</span>
    </div>
  </section>

</main>
</body>
</html>
```